Design a PRODUCT TAG for backpackers and travellers equipment/accessories company

We need a Tag Design for our products. We are a new company based in the UK called 'RoamNest'. We produce travel equipment and accessories for backpackers. Our customers are young (18-30) individuals usually GAP year makers or young professionals who enjoy travelling, adventures and exploring the world. The Tag must state our name RoamNest (at the front) and Logo(at the front) and website address www.roamnest-example.uk (on the back) and communicate our company's aim of making backpackers trip hassle free where full attention is concentrated on adventure and fun.

Target Market(s)

Young individual passionate about travelling. 18-30 age. UNI students, gap year makers or young professionals

Industry/Entity Type

Travel Industry

Colors
3276b5
33a6d7
33b8a4
abd036
fbee3d
fece3e
f68d4d
0592cd
85cae6

Requirements
Must have
• The logo and on the front
• The web address at the back
• Half of the back should be black in order to fit the product label
Nice to have
• Would be nice for the design to look like something related to travel, so for example like a plain ticket, or passport, or anything else that can be related to holiday making and travelling.

```html
<!DOCTYPE html>
<html lang="en">
<head>
<meta charset="utf-8">
<title>RoamNest Product Tag</title>
<link rel="stylesheet" href="https://fonts.googleapis.com/css2?family=Questrial&family=Roboto+Condensed:wght@700&family=Roboto:wght@700&display=swap">
<style>
  :root {
    --page: #ffffff;
    --tag-fill: #8ff1ef;
    --tag-edge: #111111;
    --ink: #3c5659;
    --ink-dark: #102a2c;
    --accent: #5bbfc0;
    --accent-deep: #3fa7a9;
    --strip-text: #a9f5f2;
    --ghost: #7fdcdb;
  }
  * { margin: 0; padding: 0; box-sizing: border-box; }
  html, body {
    width: 1200px;
    height: 497px;
    overflow: hidden;
    background: var(--page);
  }
  .tag-set { display: block; width: 1200px; height: 497px; }
  .tag-body { fill: var(--tag-fill); stroke: var(--tag-edge); stroke-width: 6; }
  .tag-hole { fill: var(--page); stroke: var(--tag-edge); stroke-width: 6; }
  .brand-name {
    font-family: "Questrial", sans-serif;
    font-size: 33px;
    fill: var(--ink);
  }
  .emblem-ring { fill: none; stroke: var(--ink-dark); stroke-width: 3; }
  .emblem-name {
    font-family: "Questrial", sans-serif;
    font-size: 28px;
    fill: var(--ink-dark);
  }
  .ghost-plane { fill: var(--ghost); }
  .pass-strip { fill: var(--accent); }
  .pass-strip-band { fill: var(--accent-deep); }
  .strip-label {
    font-family: "Roboto Condensed", sans-serif;
    font-weight: 700;
    fill: var(--ink-dark);
    font-size: 13px;
  }
  .strip-title {
    font-family: "Roboto Condensed", sans-serif;
    font-weight: 700;
    fill: var(--strip-text);
    font-size: 19px;
    letter-spacing: 1px;
  }
  .web-address {
    font-family: "Roboto", sans-serif;
    font-weight: 700;
    font-size: 15px;
    fill: var(--ink-dark);
  }
  .field-label {
    font-family: "Roboto Condensed", sans-serif;
    font-weight: 700;
    font-size: 11px;
    fill: var(--ink-dark);
  }
  .bar { fill: var(--accent); }
  .stripe-band { fill: var(--accent); }
  .plane-icon { fill: var(--accent); }
</style>
</head>
<body>
<svg class="tag-set" viewBox="0 0 1200 497" xmlns="http://www.w3.org/2000/svg">

  <!-- Front tag -->
  <g class="tag-front">
    <rect class="tag-body" x="231" y="48" width="279" height="413" rx="18"/>
    <circle class="tag-hole" cx="370" cy="84" r="15"/>
    <text class="brand-name" x="370" y="159" text-anchor="middle">RoamNest</text>
    <rect class="ghost-plane" role="img" aria-label="Faint aeroplane silhouette behind the emblem"
          x="335" y="190" width="70" height="250" rx="34" opacity="0.7"/>
    <circle class="emblem-ring" cx="370" cy="305" r="92"/>
    <text class="emblem-name" x="370" y="315" text-anchor="middle">RoamNest</text>
  </g>

  <!-- Back tag -->
  <g class="tag-back">
    <rect class="tag-body" x="640" y="48" width="310" height="413" rx="18"/>
    <rect class="ghost-plane" role="img" aria-label="Faint aeroplane silhouette across the pass"
          x="736" y="205" width="150" height="120" rx="40" opacity="0.6"/>
    <rect class="pass-strip" x="646" y="54" width="70" height="401"/>
    <rect class="pass-strip-band" x="678" y="54" width="22" height="401"/>
    <circle class="tag-hole" cx="787" cy="84" r="15"/>

    <text class="strip-label" transform="translate(668 114) rotate(-90)" text-anchor="middle">RoamNest</text>
    <text class="strip-title" transform="translate(695 300) rotate(-90)" text-anchor="middle">BOARDING PASS</text>
    <text class="strip-label" transform="translate(668 436) rotate(-90)" text-anchor="start">First Class</text>

    <text class="web-address" x="726" y="136">www.roamnest-example.uk</text>

    <rect class="bar" x="748" y="188" width="10" height="82"/>
    <rect class="bar" x="774" y="188" width="10" height="82"/>
    <rect class="bar" x="800" y="188" width="10" height="82"/>

    <text class="field-label" transform="translate(757 362) rotate(-90)">FLIGHT 123 TO:</text>
    <text class="field-label" transform="translate(783 362) rotate(-90)">PASSENGER:</text>
    <text class="field-label" transform="translate(809 362) rotate(-90)">DATE:</text>

    <rect class="stripe-band" role="img" aria-label="Diagonal stripe band" x="898" y="180" width="30" height="235"/>

    <path class="plane-icon" d="M760 424 L843 424 Q850 424 850 430 Q850 436 843 436 L760 436 L752 430 Z
                                M800 424 L784 406 L794 406 L818 424 Z
                                M800 436 L784 452 L794 452 L818 436 Z
                                M762 424 L755 413 L761 413 L772 424 Z"/>
  </g>
</svg>
</body>
</html>
```